Powerpoint Presentation design template

I am looking for a PPT presentation that show class and professionalism and in the same colour them as the logo. It should be simple, but yet classy and pro. The business is an oil and gas exploration and exploitation business. The business has nothing to do with solar panel and other renewable energies, so please no solar panel or wind farms in the background. It would be more oil rigs and LNG plant in the background of some slide templates...

oil and gas exploration and exploitation

```html
<!DOCTYPE html>
<html lang="en">
<head>
<meta charset="utf-8">
<title>Kivara Energy – Presentation Design</title>
<link href="https://fonts.googleapis.com/css2?family=Montserrat:wght@400;500;600;700&display=swap" rel="stylesheet">
<style>
:root{
  --blue:#1b8fc7;
  --green:#2bb24c;
  --teal:#1fb58a;
  --ink:#1d1d1d;
  --slide-bg:#e6ecec;
  --bar:#000000;
  --white:#ffffff;
}
*{box-sizing:border-box;margin:0;padding:0}
html,body{width:684px;height:1200px;overflow:hidden;background:#fff}
body{font-family:"Montserrat",sans-serif;color:var(--ink);position:relative}
.sheet{position:relative;width:684px;height:1200px}

.brand{display:flex;align-items:center;gap:6px}
.brand-dot{border-radius:50%;background:var(--green);flex:none}
.brand-name{font-weight:700;color:var(--blue);letter-spacing:.02em;white-space:nowrap}

.sheet-brand{position:absolute;left:0;right:0;top:34px;justify-content:center}
.sheet-brand .brand-dot{width:40px;height:40px}
.sheet-brand .brand-name{font-size:27px}
.sheet-title{position:absolute;left:0;right:0;top:100px;text-align:center;color:var(--blue);font-size:16px;font-weight:600}

.slide{position:absolute;width:279px;height:201px;overflow:hidden;background:var(--slide-bg)}
.caption{position:absolute;width:279px;text-align:center;font-size:9px;font-weight:600}

.bar{position:absolute;left:0;top:0;width:100%;height:22px;background:var(--bar);display:flex;align-items:center;justify-content:space-between;padding:0 8px}
.bar .brand-dot{width:11px;height:11px}
.bar .brand-name{font-size:8px}
.bar-label{color:var(--white);font-size:7px;font-weight:500}

.photo{position:absolute}
.dusk{background:linear-gradient(180deg,#3b3a46 0%,#6e5a5a 40%,#b07a55 62%,#8a7663 80%,#5c5048 100%)}
.sunset{background:linear-gradient(100deg,#1a1512 0%,#4a3522 40%,#c98a3a 75%,#f2c25e 100%)}

.s-heading{position:absolute;left:0;width:100%;text-align:center;color:var(--blue);font-weight:600;font-size:11px}
.s-body{font-size:6.3px;line-height:1.75}

/* slide 1 */
.cover-brand{position:absolute;left:13px;top:17px}
.cover-brand .brand-dot{width:30px;height:30px}
.cover-brand .brand-name{font-size:14px}
.cover-text{position:absolute;left:15px;top:105px;color:var(--white)}
.cover-kicker{font-size:8px;font-weight:600;margin-bottom:4px}
.cover-title{font-size:12px;line-height:1.4;font-weight:500}

/* slide 2 */
.statement{position:absolute;left:8px;display:flex;align-items:center;gap:10px;width:262px}
.statement svg{flex:none}
.statement p{font-size:6.3px;line-height:1.75}
.statement b{font-weight:600}
.tiles{position:absolute;left:8px;top:145px;display:flex;gap:6px}
.tile{position:relative;width:61px;height:44px}
.tile span{position:absolute;left:0;right:0;bottom:3px;text-align:center;color:var(--white);font-size:5px;font-weight:500}
.t-sea{background:linear-gradient(180deg,#4c6a8e,#1d3656)}
.t-drill{background:linear-gradient(180deg,#c9c7bf,#6b6456)}
.t-res{background:linear-gradient(180deg,#4f7fb4,#c49a6c)}
.t-eco{background:linear-gradient(180deg,#6e7680,#3c3f44)}

/* slide 3 */
.band{position:absolute;left:0;top:112px;width:279px;height:89px}
.band-text{position:absolute;left:13px;top:20px;color:var(--white);font-size:11px;font-weight:600;line-height:1.5}

/* slide 4 HSE */
.point{position:absolute;left:8px;display:flex;gap:7px;width:264px}
.point i{flex:none;width:7px;height:7px;border-radius:50%;background:var(--green);margin-top:1px}
.point h4{font-size:6.5px;font-weight:500;color:var(--teal)}
.point p{font-size:6.3px;line-height:1.75}
.faint-brand{position:absolute;right:8px;top:150px;opacity:.18}
.faint-brand .brand-dot{width:36px;height:36px}
.faint-brand .brand-name{font-size:18px}

/* slide exploitation */
.tech{position:absolute;left:0;top:67px;width:279px;height:134px;background:linear-gradient(180deg,#1eb67f 0%,#14a6a4 55%,#0a8fcb 100%);color:var(--white)}
.col{position:absolute;top:7px;width:130px}
.col h4{font-size:7px;font-weight:500;margin-bottom:8px}
.col li{list-style:none;position:relative;padding-left:8px;font-size:5.3px;line-height:1.65;margin-bottom:4px}
.col li::before{content:"›";position:absolute;left:0;top:0;color:#9fe3d0}

/* slide 5 */
.lead{position:absolute;left:10px;top:33px;color:var(--blue);font-size:10.5px;font-weight:500;line-height:1.5}
.map{position:absolute;left:126px;top:32px;width:138px;height:74px;border-radius:6px;background:linear-gradient(135deg,#c3c6e8,#8e93c9)}
.adv-title{position:absolute;left:10px;top:110px;color:var(--blue);font-size:10.5px;font-weight:500}
.adv{position:absolute;left:10px;display:flex;gap:5px;width:262px}
.adv i{flex:none;width:7px;height:7px;border-radius:50%;background:var(--green);margin-top:1px}
.adv p{font-size:6.2px;line-height:1.75}
.adv b{font-weight:600}

/* slide 6 */
.closing{position:absolute;left:0;right:0;top:68px;display:flex;flex-direction:column;align-items:center;gap:6px}
.closing .brand-dot{width:30px;height:30px}
.closing .brand-name{font-size:15px}
.thanks{color:var(--white);font-size:19px;font-weight:600}

.end-brand{position:absolute;left:380px;top:1000px}
.end-brand .brand-dot{width:52px;height:52px}
.end-brand .brand-name{font-size:25px}
</style>
</head>
<body>
<main class="sheet">
  <div class="brand sheet-brand"><span class="brand-dot"></span><span class="brand-name">KIVARA ENERGY</span></div>
  <h1 class="sheet-title">PPT DESIGN</h1>

  <!-- Slide 1 -->
  <section class="slide" style="left:48px;top:147px">
    <div class="photo dusk" style="inset:0" role="img" aria-label="Oil pump jacks on a field at dusk"></div>
    <div class="brand cover-brand"><span class="brand-dot"></span><span class="brand-name">KIVARA ENERGY</span></div>
    <div class="cover-text">
      <p class="cover-kicker">Title Of The Presentation</p>
      <p class="cover-title">Oil and Gas<br>Exploration &amp;<br>Exploitation Business</p>
    </div>
  </section>
  <p class="caption" style="left:40px;top:355px">Slide 1</p>

  <!-- Slide 2 -->
  <section class="slide" style="left:338px;top:147px">
    <header class="bar"><div class="brand"><span class="brand-dot"></span><span class="brand-name">KIVARA ENERGY</span></div><span class="bar-label">Company Overview</span></header>
    <div class="statement" style="top:34px">
      <svg width="22" height="22" viewBox="0 0 22 22" fill="none" stroke="#1b8fc7" stroke-width="2"><circle cx="10" cy="12" r="8"/><circle cx="10" cy="12" r="4"/><path d="M10 12 L19 3" stroke="#2bb24c"/></svg>
      <p><b>Mission Statement:</b> To responsibly explore, extract, and deliver energy solutions for a sustainable future.</p>
    </div>
    <div class="statement" style="top:62px">
      <svg width="22" height="22" viewBox="0 0 22 22" fill="none" stroke="#1b8fc7" stroke-width="2"><circle cx="13" cy="9" r="6"/><circle cx="13" cy="9" r="2" stroke="#2bb24c"/><path d="M8 14 L2 20"/></svg>
      <p><b>Vision Statement:</b> To be a global leader in oil and gas exploration and production, driving energy innovations.</p>
    </div>
    <div class="statement" style="top:92px">
      <svg width="22" height="22" viewBox="0 0 22 22" fill="none" stroke="#1b8fc7" stroke-width="1.6"><path d="M11 9 C9 6 5 7 7 10 L11 13 L15 10 C17 7 13 6 11 9Z" fill="#2bb24c" stroke="none"/><path d="M2 12 L6 18 H10 M20 12 L16 18 H12"/></svg>
      <p><b>Core Values:</b> Safety, Sustainability, Innovation, Integrity, Excellence</p>
    </div>
    <h2 class="s-heading" style="top:124px">Exploration Process</h2>
    <div class="tiles">
      <div class="tile t-sea" role="img" aria-label="Open sea seismic survey"><span>Seismic Surveys</span></div>
      <div class="tile t-drill" role="img" aria-label="Exploratory drilling rig"><span>Exploratory Drilling</span></div>
      <div class="tile t-res" role="img" aria-label="Desert drilling tower"><span>Reservoir Evaluation</span></div>
      <div class="tile t-eco" role="img" aria-label="Coastal wildlife habitat"><span>Ecosystems</span></div>
    </div>
  </section>
  <p class="caption" style="left:330px;top:355px">Slide 2</p>

  <!-- Slide 3 -->
  <section class="slide" style="left:48px;top:393px">
    <header class="bar"><div class="brand"><span class="brand-dot"></span><span class="brand-name">KIVARA ENERGY</span></div><span class="bar-label">Company Overview</span></header>
    <h2 class="s-heading" style="top:31px">The Problem / Opportunity</h2>
    <p class="s-body" style="position:absolute;left:9px;top:52px;width:261px;text-align:center">Lorem ipsum dolor sit amet, consectetuer adipiscing elit, sed diam nonummy nibh euismod tincidunt ut laoreet dolore magna aliquam erat volutpat. Ut wisi enim ad minim veniam, quis nostrud exerci tation ullamcorper suscipit lobortis nisl ut aliquip ex ea commodo consequat.</p>
    <div class="band photo sunset" role="img" aria-label="Pump jacks silhouetted against a sunset"></div>
    <p class="band-text" style="top:132px">Regulatory Changes In<br>Emissions And<br>Environmental Impact</p>
  </section>
  <p class="caption" style="left:34px;top:604px">Slide 3</p>

  <!-- Slide 4 HSE -->
  <section class="slide" style="left:338px;top:393px">
    <header class="bar"><div class="brand"><span class="brand-dot"></span><span class="brand-name">KIVARA ENERGY</span></div><span class="bar-label">Company Overview</span></header>
    <h2 class="s-heading" style="top:33px">Health, Safety &amp; Environmental Responsibility</h2>
    <div class="point" style="top:61px"><i></i><div><h4>Health and Safety Programs</h4><p>Strict safety protocols to ensure the well-being of workers &amp; communities.</p></div></div>
    <div class="point" style="top:88px"><i></i><div><h4>Environmental Impact Assessment (EIA)</h4><p>Evaluating potential environmental effects before beginning operations.</p></div></div>
    <div class="point" style="top:115px"><i></i><div><h4>Sustainability Measures</h4><p>Carbon Emission Reduction Initiatives, Waste Management Systems &amp; Spill Response Plans</p></div></div>
    <div class="brand faint-brand"><span class="brand-dot"></span><span class="brand-name">KIVARA ENERGY</span></div>
  </section>
  <p class="caption" style="left:326px;top:604px">Slide 4</p>

  <!-- Slide exploitation -->
  <section class="slide" style="left:48px;top:663px">
    <header class="bar"><div class="brand"><span class="brand-dot"></span><span class="brand-name">KIVARA ENERGY</span></div><span class="bar-label">Company Overview</span></header>
    <h2 class="s-heading" style="top:30px">Exploitation and Production</h2>
    <p class="s-body" style="position:absolute;left:0;top:50px;width:100%;text-align:center">Lorem ipsum dolor sit amet, consectetuer adipiscing elit, sed diam.</p>
    <div class="tech">
      <div class="col" style="left:8px">
        <h4>Drilling Technologies</h4>
        <ul>
          <li>Offshore (Platform and Subsea)</li>
          <li>Onshore (Land Drilling)</li>
          <li>Advanced drilling techniques (horizontal, fracking)</li>
          <li>Lorem ipsum dolor sit amet</li>
          <li>Lorem ipsum dolor sit amet doir ectetuer adipiscing elit, sed.</li>
          <li>Advanced drilling techniques (horizontal, fracking)</li>
        </ul>
      </div>
      <div class="col" style="left:147px">
        <h4>Production Stages</h4>
        <ul>
          <li>Well Completion: Installing equipment for oil/gas extraction.</li>
          <li>Extraction: Pumping oil/gas to the surface.</li>
          <li>Transportation: Pipeline or tanker systems to move resources to refineries.</li>
          <li>Lorem ipsum dolor sit amet doir ectetuer lore adipiscing elit, sed.</li>
          <li>Lorem ipsum dolor sit amet doir ectetuer lore adipiscing elit, sed.</li>
        </ul>
      </div>
    </div>
  </section>
  <p class="caption" style="left:42px;top:872px">Slide 4</p>

  <!-- Slide 5 -->
  <section class="slide" style="left:346px;top:663px">
    <header class="bar"><div class="brand"><span class="brand-dot"></span><span class="brand-name">KIVARA ENERGY</span></div><span class="bar-label">Company Overview</span></header>
    <p class="lead">Lorem Ipsum Dolor<br>Sit Amet onsectetuer<br>Adipiscing Elit, Sed<br>Diam Adipis.</p>
    <div class="map" role="img" aria-label="World map showing operating regions"></div>
    <h2 class="adv-title">Competitive Advantage</h2>
    <div class="adv" style="top:129px"><i></i><p><b>Proven Track Record:</b> Highlight successful projects or reserves discovered.</p></div>
    <div class="adv" style="top:144px"><i></i><p><b>Technological Expertise:</b> Specialized in innovative drilling, exploration, and data analysis techniques.</p></div>
    <div class="adv" style="top:170px"><i></i><p><b>Strong Partnerships:</b> Collaborations with other major industry players, governments, and financial institutions.</p></div>
  </section>
  <p class="caption" style="left:334px;top:872px">Slide 5</p>

  <!-- Slide 6 -->
  <section class="slide" style="left:49px;top:918px">
    <div class="photo dusk" style="inset:0;filter:brightness(.8)" role="img" aria-label="Oil pump jacks on a field at dusk"></div>
    <div class="closing">
      <div class="brand"><span class="brand-dot"></span><span class="brand-name">KIVARA ENERGY</span></div>
      <p class="thanks">Thank You</p>
    </div>
  </section>
  <p class="caption" style="left:40px;top:1126px">Slide 6</p>

  <div class="brand end-brand"><span class="brand-dot"></span><span class="brand-name">KIVARA<br>ENERGY</span></div>
</main>
</body>
</html>
```